Plakat-Design für Musikwettbewerb-Veranstalter
Zielgruppe
Wir veranstalten Musikwettbewerbe an Schulen. Zielgruppe sind Schüler und ihre Eltern, männlich/weiblich 40/60, u25/ü25 ca. 50/50
Aufgabenstellung
Wir sind gespannt, gerne frei denken, Logo anbei, weitere Infos auf der Homepage www.klangfuchs-wettbewerb.de, Inhalte lt. altem Plakat (ebenfalls anbei)

```html
<!DOCTYPE html>
<html lang="de">
<head>
<meta charset="utf-8">
<title>Klangfuchs – Vorentscheid Wiesenfeld</title>
<link rel="stylesheet" href="https://fonts.googleapis.com/css2?family=Montserrat:wght@900&family=Saira+Stencil+One&family=Bitter:wght@400;700&display=swap">
<style>
  :root {
    --page: #ffffff;
    --paper: #ffffff;
    --yellow: #fcec00;
    --pink: #e5197d;
    --blue: #1fa3e0;
    --orange: #f39200;
    --purple: #6b2c91;
    --green: #8cc63f;
    --ink: #1a1a1a;
  }
  * { margin: 0; padding: 0; box-sizing: border-box; }
  html, body { width: 1174px; height: 1200px; overflow: hidden; background: var(--page); }
  .poster {
    position: absolute; left: 237px; top: 105px;
    width: 700px; height: 990px;
    background: var(--paper);
    overflow: hidden;
    font-family: "Bitter", Georgia, serif;
    color: var(--ink);
  }
  .instrument-art {
    position: absolute; left: 18px; top: 0; width: 664px; height: 320px;
    background:
      radial-gradient(ellipse at 15% 70%, var(--pink) 0 28%, transparent 45%),
      radial-gradient(ellipse at 38% 20%, var(--orange) 0 22%, transparent 40%),
      radial-gradient(ellipse at 55% 55%, var(--purple) 0 22%, transparent 40%),
      radial-gradient(ellipse at 72% 40%, var(--green) 0 22%, transparent 40%),
      radial-gradient(ellipse at 90% 55%, var(--yellow) 0 26%, transparent 44%);
    border-radius: 40% 40% 30% 30% / 50% 50% 20% 20%;
  }
  .crowd-art {
    position: absolute; left: 0; top: 505px; width: 700px; height: 200px;
    background: linear-gradient(to bottom, rgba(252,236,0,0) 0%, rgba(252,236,0,.55) 45%, var(--yellow) 100%);
  }
  .footer-field { position: absolute; left: 0; top: 700px; width: 700px; height: 290px; background: var(--yellow); }
  .event-title {
    position: absolute; left: 0; top: 128px; width: 700px; text-align: center;
    font-family: "Montserrat", Arial, sans-serif; font-weight: 900;
    font-size: 106px; letter-spacing: -3px; color: #fff; line-height: 1;
  }
  .tag {
    font-family: "Saira Stencil One", Impact, sans-serif;
    color: #fff; line-height: 1; white-space: nowrap; text-align: center;
  }
  .tag--date { position: absolute; left: 72px; top: 293px; width: 276px; height: 54px; background: var(--pink); font-size: 46px; padding-top: 4px; transform: rotate(-1deg); }
  .tag--round { position: absolute; left: 10px; top: 340px; width: 670px; height: 100px; background: var(--blue); font-size: 86px; padding-top: 7px; transform: rotate(1deg); }
  .tag-row {
    position: absolute; left: 0; top: 432px; width: 700px;
    display: flex; justify-content: center; align-items: center; gap: 12px;
  }
  .tag--town { height: 66px; background: var(--blue); font-size: 52px; padding: 7px 14px 0; }
  .tag--time { height: 46px; background: var(--pink); font-size: 32px; padding: 6px 12px 0; transform: rotate(-1deg); }
  .schools { position: absolute; left: 0; top: 515px; width: 700px; list-style: none; text-align: center; }
  .schools li {
    font-family: "Saira Stencil One", Impact, sans-serif; font-size: 33px;
    color: var(--ink); line-height: 62px; letter-spacing: 1px; white-space: nowrap;
  }
  .info { position: absolute; top: 712px; font-size: 19px; line-height: 25px; text-align: center; }
  .info--venue { left: 40px; width: 290px; }
  .info--venue strong { font-weight: 700; }
  .info--tickets { left: 400px; width: 250px; }
  .apply { position: absolute; left: 0; top: 836px; width: 700px; text-align: center; font-size: 17px; color: var(--blue); white-space: nowrap; }
  .web { position: absolute; left: 0; top: 884px; width: 700px; text-align: center; font-size: 17px; white-space: nowrap; }
  .partners {
    position: absolute; left: 30px; top: 934px; width: 640px;
    display: flex; justify-content: space-between; align-items: center;
    list-style: none; font-size: 16px; font-weight: 700;
  }
  .partners li { display: flex; align-items: center; gap: 5px; white-space: nowrap; }
  .partner-mark { width: 12px; height: 12px; background: var(--ink); }
</style>
</head>
<body>
<main class="poster">
  <div class="instrument-art" role="img" aria-label="Farbige Illustration aus Musikinstrumenten: Gitarren, Tuba, Mikrofon, Keyboard, Flügel und Schlagzeug mit Farbspritzern"></div>
  <div class="crowd-art" role="img" aria-label="Silhouette einer jubelnden Menschenmenge in Gelb"></div>
  <div class="footer-field"></div>

  <h1 class="event-title">Klangfuchs</h1>
  <div class="tag tag--date">24.06.2017</div>
  <div class="tag tag--round">VORENTSCHEID</div>
  <div class="tag-row">
    <div class="tag tag--town">WIESENFELD</div>
    <div class="tag tag--time">AB 19:00 UHR</div>
  </div>

  <ul class="schools">
    <li>LINDENHOF-SCHULE</li>
    <li>BERUFLICHE SCHULE WIESENFELD</li>
    <li>GEMEINSCHAFTSSCHULE WIESENFELD</li>
  </ul>

  <p class="info info--venue"><strong>Mensa der<br>Lindenhof-Schule</strong><br>Lindenhof-Straße 5<br>24999 Wiesenfeld</p>
  <p class="info info--tickets">Einlass: 18:30 Uhr<br>Beginn: 19:00 Uhr<br>Vvk: 3 € | Ak: 4 €</p>

  <p class="apply">Bewerbung für Künstler unter www.klangfuchs-wettbewerb.de/bewerbung</p>
  <p class="web">www.klangfuchs-wettbewerb.de | www.treffpunkt-social.de/klangfuchs</p>

  <ul class="partners">
    <li><span class="partner-mark"></span>Kreisbank</li>
    <li>Tonwerk</li>
    <li>Notenrat</li>
    <li>Saitenhaus</li>
    <li>Landesamt Bildung</li>
  </ul>
</main>
</body>
</html>
```